Rack Card Design Project

We are a locally family owned public golf course. We would like to have a rack card designed that can be used for multiple applications. The colors in our logo are grey, blue, and white. Please use those in the card design. The company logo, contact information, address, and summer pricing should be included. I've included some pictures that may or may not be used. I'm also open to suggestions....use one photo, multiple photos, a stock photo or image representing golf etc.

```html
<!DOCTYPE html>
<html lang="en">
<head>
<meta charset="utf-8">
<title>Harbor Pines Golf Club – Summer Rates Rack Card</title>
<link href="https://fonts.googleapis.com/css2?family=Libre+Baskerville:wght@700&family=Encode+Sans+Condensed:wght@600;700&family=Montserrat:wght@500;600;700&display=swap" rel="stylesheet">
<style>
  :root {
    --navy: #133560;
    --grey: #8a8a8a;
    --grey-dark: #4a4a4a;
    --grey-line: #9a9a9a;
    --white: #ffffff;
    --backdrop: #d9d9d9;
  }
  * { box-sizing: border-box; margin: 0; padding: 0; }
  html, body { width: 1200px; height: 903px; overflow: hidden; }
  body {
    background: var(--backdrop);
    font-family: "Montserrat", sans-serif;
    position: relative;
  }
  .rack-card {
    position: absolute;
    left: 400px; top: 22px;
    width: 400px; height: 860px;
    background: var(--white);
    overflow: hidden;
    box-shadow: 0 8px 24px rgba(0,0,0,.18);
  }
  .hero-photo {
    position: absolute; left: 0; top: 0;
    width: 400px; height: 350px;
  }
  .club-mark {
    position: absolute;
    left: 132px; top: 282px;
    width: 136px; height: 136px;
    border-radius: 50%;
    background: var(--white);
    border: 6px solid var(--grey-line);
    display: flex; align-items: center; justify-content: center;
    text-align: center;
  }
  .club-mark__name {
    font-family: "Montserrat", sans-serif;
    font-weight: 700;
    font-size: 14px;
    line-height: 1.25;
    color: var(--navy);
    text-transform: uppercase;
  }
  .rates-title {
    position: absolute; top: 428px; left: 0; width: 100%;
    text-align: center;
    font-family: "Libre Baskerville", serif;
    font-weight: 700;
    font-size: 32px;
    line-height: 1.2;
    color: var(--navy);
    letter-spacing: -0.5px;
  }
  .rates-season {
    position: absolute; top: 472px; left: 0; width: 100%;
    text-align: center;
    font-family: "Encode Sans Condensed", sans-serif;
    font-weight: 700;
    font-size: 23px;
    line-height: 1.2;
    color: var(--grey-dark);
  }
  .rate-table {
    position: absolute; top: 510px; left: 36px;
    width: 328px;
    display: flex; flex-direction: column; gap: 3px;
    font-size: 14px; font-weight: 500;
  }
  .rate-table__heading {
    background: var(--navy); color: var(--white);
    border-radius: 5px;
    height: 26px; line-height: 26px; text-align: center;
  }
  .rate-row { display: grid; grid-template-columns: 1fr 1fr; height: 26px; }
  .rate-row__label {
    background: var(--navy); color: var(--white);
    line-height: 26px; text-align: center;
    border-radius: 5px 0 0 5px;
  }
  .rate-row__price {
    background: var(--grey); color: var(--white);
    line-height: 26px; text-align: center;
    border-radius: 0 5px 5px 0;
    border-left: 2px solid var(--white);
  }
  .rate-table__note {
    margin-top: 3px;
    background: var(--navy); color: var(--white);
    border-radius: 5px;
    height: 27px; line-height: 27px; text-align: center;
    font-size: 13px;
  }
  .rate-table__note strong { font-weight: 700; }
  .lunch {
    position: absolute; top: 721px; left: 0; width: 100%;
    text-align: center;
    font-family: "Encode Sans Condensed", sans-serif;
    font-weight: 700;
    line-height: 1.1;
  }
  .lunch__label { font-size: 22px; color: var(--grey-dark); }
  .lunch__hours { font-size: 22px; color: var(--navy); }
  .contact-band {
    position: absolute; left: 0; bottom: 0;
    width: 100%; height: 82px;
    background: var(--navy);
    border-top: 3px solid var(--grey-line);
    color: var(--white);
    text-align: center;
    padding-top: 12px;
    font-size: 11.5px;
    line-height: 1.5;
  }
  .contact-band__name { font-weight: 700; font-size: 12.5px; }
  .contact-band__line { display: flex; justify-content: center; align-items: center; gap: 5px; }
  .contact-band__line + .contact-band__line { gap: 16px; }
  .contact-item { display: inline-flex; align-items: center; gap: 5px; }
  .icon { width: 10px; height: 10px; fill: none; stroke: var(--white); stroke-width: 1.6; }
</style>
</head>
<body>
  <article class="rack-card">
    <svg class="hero-photo" viewBox="0 0 400 350" role="img" aria-label="Photo of a golf course fairway with tall pine trees and a flagstick at sunset">
      <defs>
        <linearGradient id="sky" x1="0" y1="0" x2="0" y2="1">
          <stop offset="0" stop-color="#dedcd6"/>
          <stop offset="0.55" stop-color="#f1e3bd"/>
          <stop offset="0.72" stop-color="#5c6a34"/>
          <stop offset="1" stop-color="#6f9040"/>
        </linearGradient>
      </defs>
      <path d="M0 0 H400 V328 Q200 240 0 328 Z" fill="url(#sky)"/>
      <path d="M0 336 Q200 248 400 336" fill="none" stroke="#9a9a9a" stroke-width="5"/>
    </svg>

    <div class="club-mark">
      <span class="club-mark__name">Harbor Pines<br>Golf Club</span>
    </div>

    <h1 class="rates-title">SUMMER RATES</h1>
    <p class="rates-season">MAY 1 – SEPTEMBER 30</p>

    <section class="rate-table">
      <div class="rate-table__heading">18 Holes With Cart</div>
      <div class="rate-row"><span class="rate-row__label">7AM - 11AM</span><span class="rate-row__price">$24</span></div>
      <div class="rate-row"><span class="rate-row__label">11AM - 3PM</span><span class="rate-row__price">$19</span></div>
      <div class="rate-row"><span class="rate-row__label">3PM - Close</span><span class="rate-row__price">$15</span></div>
      <div class="rate-row"><span class="rate-row__label">9 Holes With Cart</span><span class="rate-row__price">$15</span></div>
      <div class="rate-row"><span class="rate-row__label">Walking</span><span class="rate-row__price">$12</span></div>
      <div class="rate-table__note">Children 15 and Under <strong>FREE</strong> with Paid Adult</div>
    </section>

    <div class="lunch">
      <div class="lunch__label">LUNCH AVAILABLE DAILY</div>
      <div class="lunch__hours">10AM – 3PM</div>
    </div>

    <footer class="contact-band">
      <div class="contact-band__name">Harbor Pines Golf Club</div>
      <div class="contact-band__line">
        <svg class="icon" viewBox="0 0 10 10"><path d="M5 9.2 C2.5 6 2 5 2 3.8 A3 3 0 0 1 8 3.8 C8 5 7.5 6 5 9.2 Z"/><circle cx="5" cy="3.8" r="1"/></svg>
        <span>4410 Heron Bay Road, Palm Cove, FL 34000</span>
      </div>
      <div class="contact-band__line">
        <span class="contact-item">
          <svg class="icon" viewBox="0 0 10 10"><path d="M2 1 L3.8 1 L4.4 3.2 L3.2 4.2 Q4.2 6 5.8 6.8 L6.8 5.6 L9 6.2 L9 8 Q5 9 2 5 Q1 3 2 1 Z"/></svg>
          555-014-2287
        </span>
        <span class="contact-item">
          <svg class="icon" viewBox="0 0 10 10"><circle cx="5" cy="5" r="4"/><path d="M1 5 H9 M5 1 Q2.5 5 5 9 M5 1 Q7.5 5 5 9"/></svg>
          www.harborpinesgc.com
        </span>
      </div>
    </footer>
  </article>
</body>
</html>
```